Play on Words (French Puns)

Cover (11 x 17.8 cm) for a book of French plays on words. (Author: "Mathis Lobry" Title: "The Tricksters" Subtitle "Verbal Treats To Nibble" Publisher (at the bottom of the page): "Quill Press"

Target Market(s)

General public

Industry/Entity Type

Book Publisher

Colors

Designer to choose colors to be used in the design.

Requirements
Must have
• "Unserious" look
Should not have
• Eiffel Tower, triumphal arch (it's a book on French language, not on France)

```html
<!DOCTYPE html>
<html lang="en">
<head>
<meta charset="utf-8">
<title>The Tricksters — Mathis Lobry</title>
<link href="https://fonts.googleapis.com/css2?family=Chewy&family=Roboto:wght@400;500&display=swap" rel="stylesheet">
<style>
  :root {
    --page-bg: #f2f2f0;
    --cover-white: #ffffff;
    --ink: #1a1a1a;
    --accent-blue: #0a6cc2;
    --accent-red: #e8141c;
    --band-blue: #0257a8;
    --band-text: #ffffff;
    --title-pink: #f4606a;
    --title-violet: #c15fd6;
    --title-orange: #f27418;
    --title-yellow: #fbb40c;
    --title-cyan: #2fb6e0;
    --title-crimson: #c4303a;
    --title-green: #80ad10;
    --art-blue: #2eafd1;
    --art-red: #e8262a;
    --art-skin: #e7b898;
  }
  * { box-sizing: border-box; margin: 0; padding: 0; }
  html, body {
    width: 1200px;
    height: 800px;
    overflow: hidden;
    background: var(--page-bg);
    font-family: "Roboto", Arial, sans-serif;
  }
  .stage {
    width: 1200px;
    height: 800px;
    display: flex;
    align-items: center;
    justify-content: center;
  }
  .book-cover {
    position: relative;
    width: 460px;
    height: 744px;
    background: var(--cover-white);
    box-shadow: 0 6px 24px rgba(0,0,0,0.12);
    display: flex;
    flex-direction: column;
    align-items: center;
  }
  .author {
    margin-top: 42px;
    font-size: 30px;
    font-weight: 400;
    letter-spacing: 0.11em;
    color: var(--ink);
    text-transform: uppercase;
  }
  .title {
    margin-top: 34px;
    font-family: "Chewy", "Comic Sans MS", cursive;
    font-weight: 400;
    text-align: center;
    text-transform: uppercase;
    line-height: 0.98;
    color: var(--ink);
  }
  .title-line { display: block; white-space: nowrap; }
  .title-line--short { font-size: 62px; letter-spacing: 0.02em; }
  .title-line--long { font-size: 58px; letter-spacing: 0; }
  .title .l1 { color: var(--title-pink); }
  .title .l2 { color: var(--title-violet); }
  .title .l3 { color: var(--title-orange); }
  .title .l4 { color: var(--title-yellow); }
  .title .l5 { color: var(--title-cyan); }
  .title .l6 { color: var(--title-crimson); }
  .title .l7 { color: var(--title-green); }
  .title .tilt-a { display: inline-block; transform: rotate(-6deg) translateY(2px); }
  .title .tilt-b { display: inline-block; transform: rotate(5deg) translateY(-3px); }
  .cover-illustration {
    margin-top: 26px;
    width: 300px;
    height: 240px;
    border-radius: 14px;
    background: linear-gradient(160deg, var(--art-red) 0%, var(--art-skin) 38%, var(--art-blue) 70%, #4a4a4a 100%);
    opacity: 0.8;
  }
  .subtitle {
    margin-top: 40px;
    font-size: 26px;
    font-weight: 400;
    color: var(--ink);
  }
  .subtitle .word-blue { color: var(--accent-blue); }
  .subtitle .word-red { color: var(--accent-red); }
  .publisher-band {
    position: absolute;
    left: 0;
    right: 0;
    bottom: 0;
    height: 68px;
    background: var(--band-blue);
    display: flex;
    align-items: center;
    justify-content: center;
  }
  .publisher {
    color: var(--band-text);
    font-size: 16px;
    font-weight: 500;
    letter-spacing: 0.14em;
    text-transform: uppercase;
  }
</style>
</head>
<body>
  <main class="stage">
    <article class="book-cover">
      <p class="author">Mathis Lobry</p>
      <h1 class="title">
        <span class="title-line title-line--short"><span class="l1 tilt-a">T</span><span class="l2">h</span><span class="l3 tilt-b">e</span></span>
        <span class="title-line title-line--long"><span class="l2 tilt-a">T</span><span class="l4">r</span><span class="l5 tilt-b">i</span><span class="l6">c</span><span class="l3 tilt-a">k</span><span class="l5">s</span><span class="l1 tilt-b">t</span><span class="l4">e</span><span class="l7 tilt-a">r</span><span class="l5">s</span></span>
      </h1>
      <div class="cover-illustration" role="img" aria-label="Cartoon of friends in a blue convertible heading to the beach with an umbrella, beach ball and flying hat, sunglasses and shoe"></div>
      <p class="subtitle"><span class="word-blue">Verbal</span> Treats To <span class="word-red">Nibble</span></p>
      <footer class="publisher-band">
        <p class="publisher">Quill Press</p>
      </footer>
    </article>
  </main>
</body>
</html>
```